Mobile phone signal boosting solutions needs a website

We need a website design for the reselling of a mobile signal boosting product set. These solutions are Vexlor exempt and will provide an indoor signal for mobile phones. We would like to see designs that incorporate the colours and feel of our logo. The domain will be
openmeadow.com / co.uk
Overview of the company and how it is to be used: Open meadow (domain name) will work with business and end user to provide mobile signal boosting – where people struggle indoors with a mobile signal our solutions will help by finding the smallest signal and boosting it, allowing users to use voice and data over their mobile network (please note this is not wireless signal boosting)
Number of Pages:
-Home
-Solutions / How it works
-Case Studies
-Contact
Text content: Currently just use placeholders
Technical specs : Wordpress and ability to use CMS if that’s relevant
Target Market(s)
Business professional all markets /high end residential
Coded - Design and coding required
4 page

```html
<!DOCTYPE html>
<html lang="en">
<head>
<meta charset="utf-8">
<title>Open Meadow – Mobile Signal Booster</title>
<link rel="stylesheet" href="https://fonts.googleapis.com/css2?family=Montserrat:wght@400;500;600;700&family=Roboto:wght@300;400;500&display=swap">
<style>
:root{
  --yellow:#fcc100;
  --black:#0c0c0c;
  --dark:#111111;
  --panel:#1b1b1b;
  --panel-2:#222222;
  --white:#ffffff;
  --muted:#cfcfcf;
  --head:'Roboto',Arial,sans-serif;
  --body:'Montserrat',Arial,sans-serif;
}
*{margin:0;padding:0;box-sizing:border-box}
html,body{width:1200px;height:4332px;overflow:hidden;background:var(--black);color:var(--white);font-family:var(--body)}
.page{position:relative;width:1200px;height:4332px;overflow:hidden}
section,header,footer{position:absolute;left:0;width:1200px;overflow:hidden}
.abs{position:absolute}
.btn{position:absolute;display:flex;align-items:center;justify-content:center;background:var(--yellow);color:#111;border-radius:20px;font:600 12px var(--body)}
.label{position:absolute;left:0;width:1200px;text-align:center;color:var(--yellow);font:500 11px var(--body);text-transform:uppercase}
.heading{position:absolute;left:0;width:1200px;text-align:center;font:300 32px var(--head);color:var(--white)}
.rule{position:absolute;left:576px;width:48px;height:12px}
.photo{position:absolute}

/* top bar */
.topbar{top:0;height:30px;background:var(--yellow);color:#111;font:500 9px var(--body)}
/* nav */
.nav{top:30px;height:74px;background:var(--dark)}
.brand{position:absolute;display:flex;align-items:center;gap:8px;font:500 22px var(--head);color:var(--white)}
.brand .dot{width:14px;height:14px;background:var(--yellow)}
.menu a{position:absolute;top:30px;font:500 11px var(--body);color:var(--white);text-decoration:none}
.menu a.active{color:var(--yellow)}

/* hero */
.hero{top:104px;height:543px;background:radial-gradient(ellipse at 75% 40%,#2c2c2c 0%,#1a1a1a 45%,#121212 100%)}
.hero-form{top:568px;left:161px;width:876px;height:79px;background:#1c1c1c;border-radius:6px;position:absolute}
.field{position:absolute;border:1px solid #7a7a7a;border-radius:20px;height:37px;display:flex;align-items:center;padding-left:24px;font:400 9px var(--body);color:#bdbdbd}

/* about */
.about{top:647px;height:513px;background:var(--black)}
.about p{font:400 10.5px/20px var(--body);color:#e6e6e6;text-align:justify}

/* solutions */
.solutions{top:1160px;height:566px;background:linear-gradient(180deg,#0c0c0c 0%,#161616 60%,#101010 100%)}
.card{position:absolute;top:180px;width:210px;text-align:center}
.card .img{height:150px;border-radius:3px}
.card h3{margin-top:20px;font:400 18px var(--head)}
.card p{margin-top:12px;font:400 9.5px/18px var(--body);color:#ddd;padding:0 6px}

/* how it works */
.how{top:1726px;height:728px;background:var(--black)}
.feat{position:absolute;width:230px}
.feat h4{font:400 13px var(--head);color:var(--yellow);text-transform:uppercase;margin-bottom:10px}
.feat p{font:400 9.5px/21px var(--body);color:#e8e8e8}
.feat.right{text-align:right}
.icon{position:absolute;width:74px;height:74px;border:2px solid var(--yellow);border-radius:50%;display:flex;align-items:center;justify-content:center}
.icon.solid{background:var(--yellow)}

/* testimonials */
.testi{top:2454px;height:546px;background:linear-gradient(180deg,#151515,#101010)}
.review{position:absolute;top:162px;width:377px;height:218px;background:var(--panel)}
.review .avatar{position:absolute;left:20px;top:24px;width:82px;height:82px;border-radius:50%;border:3px solid #d9d9d9}
.review .name{position:absolute;left:120px;top:30px;font:700 15px var(--body);color:var(--yellow)}
.review .role{position:absolute;left:120px;top:54px;font:400 12px var(--body);color:#fff}
.review .stars{color:var(--yellow);font-size:11px;letter-spacing:1px;margin-left:10px}
.review p{position:absolute;left:120px;top:82px;width:236px;font:400 9.5px/21px var(--body);color:#ddd;text-align:justify}
.review .quote{position:absolute;left:28px;top:115px;font:300 80px/1 var(--head);color:var(--yellow);font-style:normal}
.review .corner{position:absolute;right:0;bottom:0;width:15px;height:15px;background:#8a6d10}

/* case studies */
.cases{top:3000px;height:580px;background:var(--black)}
.case{position:absolute;background:var(--panel);padding:20px 16px}
.case .date{font:600 9px var(--body);color:var(--yellow)}
.case h5{margin-top:10px;font:400 13.5px/21px var(--head);text-transform:uppercase;color:#fff}
.case p{margin-top:8px;font:400 9.5px/18px var(--body);color:#ddd}
.case .more{margin-top:6px;font:700 9px var(--body);color:var(--yellow)}

/* contact */
.contact{top:3580px;height:522px;background:var(--black)}
.contact-box{position:absolute;left:235px;top:162px;width:730px;height:316px;background:var(--yellow)}
.input{position:absolute;background:#fff6d6;border:1px solid #e8cf6e;font:400 9.5px var(--body);color:#8b7a3a;padding:16px 0 0 16px}

/* footer */
.footer{top:4102px;height:230px;background:#0e0e0e}
.fcol h6{font:700 12px var(--body);color:#fff;margin-bottom:14px}
.fcol li{list-style:none;font:400 9.5px var(--body);color:#fff;margin-bottom:11px}
.fcol li::before{content:"»";margin-right:8px}
.fcol.plain li::before{content:none}
</style>
</head>
<body>
<div class="page">

<!-- Top bar -->
<div class="topbar abs" style="left:0;width:1200px">
  <div class="abs" style="left:182px;top:10px;display:flex;align-items:center;gap:4px">
    <svg width="8" height="10" viewBox="0 0 8 10"><path d="M4 0a4 4 0 0 1 4 4c0 3-4 6-4 6S0 7 0 4a4 4 0 0 1 4-4z" fill="#111"/><circle cx="4" cy="4" r="1.4" fill="#fcc100"/></svg>
    location : 123 Lorem ipsum dolor sit amet
  </div>
  <div class="abs" style="left:751px;top:10px;display:flex;align-items:center;gap:4px">
    <svg width="10" height="8" viewBox="0 0 10 8"><rect width="10" height="8" rx="1" fill="#111"/><path d="M0 1l5 3.5L10 1" stroke="#fcc100" fill="none"/></svg>
    Email Address : hello@openmeadow.com
  </div>
  <div class="abs" style="left:933px;top:7px;width:1px;height:16px;background:#111"></div>
  <svg class="abs" style="left:955px;top:7px" width="82" height="16" viewBox="0 0 82 16">
    <g fill="none" stroke="#111" stroke-width="1.2"><circle cx="8" cy="8" r="7"/><circle cx="30" cy="8" r="7"/><circle cx="52" cy="8" r="7"/><circle cx="74" cy="8" r="7"/></g>
  </svg>
</div>

<!-- Navigation -->
<header class="nav">
  <div class="brand" style="left:161px;top:22px"><span class="dot"></span>Open Meadow</div>
  <nav class="menu">
    <a class="active" style="left:439px">Home</a>
    <a style="left:501px">Solutions</a>
    <a style="left:578px">How it works</a>
    <a style="left:676px">Case Studies</a>
    <a style="left:773px">Contact</a>
  </nav>
  <div class="abs" style="left:852px;top:19px;width:35px;height:35px;border-radius:50%;background:var(--yellow);display:flex;align-items:center;justify-content:center">
    <svg width="16" height="16" viewBox="0 0 24 24"><path d="M6.6 10.8a15 15 0 0 0 6.6 6.6l2.2-2.2a1 1 0 0 1 1-.25 11.4 11.4 0 0 0 3.6.57 1 1 0 0 1 1 1V20a1 1 0 0 1-1 1A17 17 0 0 1 3 4a1 1 0 0 1 1-1h3.5a1 1 0 0 1 1 1c0 1.25.2 2.45.57 3.57a1 1 0 0 1-.25 1z" fill="#111"/></svg>
  </div>
  <div class="abs" style="left:898px;top:22px;font:600 9px var(--body);color:var(--yellow)">Call Us Today :</div>
  <div class="abs" style="left:898px;top:34px;font:600 18px var(--body);color:#fff">+1 888 888 8888</div>
</header>

<!-- Hero -->
<section class="hero">
  <div class="abs" style="left:161px;top:121px;font:600 11px var(--body);color:var(--yellow)">WELCOME TO</div>
  <h1 class="abs" style="left:158px;top:134px;font:400 66px var(--head);color:#fff;white-space:nowrap">Open Meadow</h1>
  <p class="abs" style="left:161px;top:219px;width:420px;font:400 10px/20px var(--body);color:#eee">Lorem ipsum dolor sit amet, consectetur adipiscing elit, sed do eiusmod tempor incididunt ut labore et dolore magna aliqua.</p>
  <div class="btn" style="left:161px;top:273px;width:138px;height:38px">Request Survey</div>
  <div class="photo" role="img" aria-label="Signal strength decoration over a dark network pattern" style="left:694px;top:56px;width:370px;height:336px;background:radial-gradient(ellipse at 50% 55%,rgba(252,193,0,.28) 0%,rgba(255,255,255,.08) 45%,rgba(0,0,0,0) 72%)"></div>
</section>

<div class="hero-form">
  <div class="field" style="left:59px;top:22px;width:195px">Full Name *</div>
  <div class="field" style="left:266px;top:22px;width:195px">Email Address *</div>
  <div class="field" style="left:471px;top:22px;width:195px">Phone Number *</div>
  <div class="btn" style="left:681px;top:22px;width:138px;height:37px">Request Survey</div>
</div>

<!-- About -->
<section class="about">
  <div class="abs" style="left:156px;top:54px;width:220px;height:381px;border:5px solid var(--yellow)"></div>
  <div class="photo" role="img" aria-label="Businesswoman in a dark suit looking at her smartphone in a city setting" style="left:164px;top:62px;width:255px;height:375px;background:linear-gradient(160deg,#b9a24a 0%,#4f4a3a 40%,#2a2a2d 70%,#7a7770 100%)"></div>
  <div class="photo" role="img" aria-label="Faint signal strength decoration" style="left:420px;top:160px;width:160px;height:280px;background:linear-gradient(180deg,rgba(160,150,60,.45),rgba(60,60,40,.25))"></div>
  <div class="abs" style="left:615px;top:69px;font:500 11px var(--body);color:var(--yellow)">ABOUT OPEN MEADOW</div>
  <h2 class="abs" style="left:614px;top:82px;font:300 30px var(--head);white-space:nowrap">Mobile Signal Booster</h2>
  <svg class="abs" style="left:615px;top:124px" width="40" height="12" viewBox="0 0 40 12"><path d="M0 10h40M8 5h24" stroke="#fcc100" stroke-width="2"/></svg>
  <p class="abs" style="left:615px;top:140px;width:407px">Lorem ipsum dolor sit amet, consectetur adipiscing elit, sed do eiusmod tempor incididunt ut labore et dolore magna aliqua. Quis ipsum suspendisse ultrices gravida. Risus commodo viverra maecenas accumsan lacus vel facilisis. unde omnis iste natus error sit voluptatem accusantium doloremque laudantium, totam rem aperiam, eaque ipsa quae ab illo inventore veritatis et quasi architecto beatae vitae dicta sunt explicabo. Nemo enim ipsam voluptatem quia voluptas sit aspernatur aut odit aut fugit, sed quia consequuntur magni dolores eos qui ratione voluptatem sequi nesciunt. Neque porro quisquam est, qui dolorem ipsum quia dolor sit amet, consectetur, adipisci velit, sed quia non numquam eius modi tempora incidunt ut labore et dolore magnam aliquam quaerat voluptatem. Ut enim ad minima veniam, quis nostrum exercitationem ullam corporis suscipit laboriosam, nisi ut aliquid ex ea commodi consequatur.</p>
  <div class="btn" style="left:615px;top:393px;width:140px;height:37px">Learn More</div>
</section>

<!-- Solutions -->
<section class="solutions">
  <div class="label" style="top:80px">Our Solution</div>
  <h2 class="heading" style="top:92px">Eiusmod Tempor Incididunt Ut Labore Et Dolore</h2>
  <svg class="rule" style="top:138px" viewBox="0 0 48 12"><path d="M4 10h40M14 4h20" stroke="#fcc100" stroke-width="2"/></svg>
  <div class="card" style="left:161px">
    <div class="img" role="img" aria-label="Hands holding a smartphone against a white background" style="background:linear-gradient(135deg,#f2f2f2,#b8bcc3 60%,#5d636d)"></div>
    <h3>Lorem ipsum dolor</h3>
    <p>Lorem ipsum dolor sit amet, consectetur adipiscing elit, sed do eiusmod tempor incididunt ut labore et dolore magna aliquauis ipsum suspendisse ultrices gravidaisus commodo.</p>
  </div>
  <div class="card" style="left:383px">
    <div class="img" role="img" aria-label="Hand touching a tablet with a glowing blue city network" style="background:linear-gradient(135deg,#0e2a4a,#2f7bbf 55%,#9fd5ff)"></div>
    <h3>Lorem ipsum dolor</h3>
    <p>Lorem ipsum dolor sit amet, consectetur adipiscing elit, sed do eiusmod tempor incididunt ut labore et dolore magna aliquauis ipsum suspendisse ultrices gravidaisus commodo.</p>
  </div>
  <div class="card" style="left:605px">
    <div class="img" role="img" aria-label="Blue skyscrapers with digital connection lines" style="background:linear-gradient(160deg,#0a1c4a,#1f55b5 50%,#6aa9ff)"></div>
    <h3>Lorem ipsum dolor</h3>
    <p>Lorem ipsum dolor sit amet, consectetur adipiscing elit, sed do eiusmod tempor incididunt ut labore et dolore magna aliquauis ipsum suspendisse ultrices gravidaisus commodo.</p>
  </div>
  <div class="card" style="left:827px">
    <div class="img" role="img" aria-label="Businessman reading his phone by a sketched wall" style="background:linear-gradient(135deg,#d9d3c8,#9a8f80 55%,#4c4740)"></div>
    <h3>Lorem ipsum dolor</h3>
    <p>Lorem ipsum dolor sit amet, consectetur adipiscing elit, sed do eiusmod tempor incididunt ut labore et dolore magna aliquauis ipsum suspendisse ultrices gravidaisus commodo.</p>
  </div>
</section>

<!-- How it works -->
<section class="how">
  <div class="label" style="top:60px">How its work</div>
  <h2 class="heading" style="top:86px">Eiusmod Tempor Incididunt Ut Labore Et Dolore</h2>
  <svg class="rule" style="top:122px" viewBox="0 0 48 12"><path d="M4 10h40M14 4h20" stroke="#fcc100" stroke-width="2"/></svg>
  <svg class="abs" style="left:0;top:0" width="1200" height="728" viewBox="0 0 1200 728">
    <circle cx="600" cy="582" r="438" fill="none" stroke="#fcc100" stroke-width="2.5"/>
    <circle cx="600" cy="590" r="452" fill="none" stroke="#6b5410" stroke-width="1"/>
    <g stroke="#bdbdbd" stroke-width="1.5" stroke-dasharray="2 3">
      <line x1="277" y1="384" x2="580" y2="384"/><line x1="640" y1="384" x2="916" y2="384"/>
      <line x1="272" y1="530" x2="580" y2="530"/><line x1="640" y1="530" x2="916" y2="530"/>
    </g>
  </svg>
  <div class="photo" role="img" aria-label="Central signal strength decoration" style="left:415px;top:300px;width:311px;height:336px;background:radial-gradient(ellipse at 50% 55%,rgba(252,193,0,.32) 0%,rgba(255,255,255,.06) 50%,rgba(0,0,0,0) 72%)"></div>

  <div class="icon solid" style="left:249px;top:266px"><svg width="30" height="30" viewBox="0 0 24 24" fill="none" stroke="#fff" stroke-width="1.6"><circle cx="12" cy="7" r="4"/><path d="M4 21c0-4.5 3.5-7 8-7s8 2.5 8 7"/></svg></div>
  <div class="icon" style="left:866px;top:266px"><svg width="30" height="30" viewBox="0 0 24 24"><path d="M6.6 10.8a15 15 0 0 0 6.6 6.6l2.2-2.2a1 1 0 0 1 1-.25 11.4 11.4 0 0 0 3.6.57 1 1 0 0 1 1 1V20a1 1 0 0 1-1 1A17 17 0 0 1 3 4a1 1 0 0 1 1-1h3.5a1 1 0 0 1 1 1c0 1.25.2 2.45.57 3.57a1 1 0 0 1-.25 1z" fill="none" stroke="#fcc100" stroke-width="1.5"/></svg></div>
  <div class="icon" style="left:176px;top:417px"><svg width="30" height="30" viewBox="0 0 24 24" fill="none" stroke="#fcc100" stroke-width="1.8"><circle cx="12" cy="12" r="9"/><path d="M7.5 12.5l3 3 6-6.5"/></svg></div>
  <div class="icon" style="left:945px;top:417px"><svg width="30" height="30" viewBox="0 0 24 24" fill="none" stroke="#fcc100" stroke-width="1.6"><path d="M3 12l9-9h8v8l-9 9z"/><circle cx="16" cy="8" r="1.6"/></svg></div>
  <div class="icon" style="left:164px;top:571px"><svg width="30" height="30" viewBox="0 0 24 24" fill="none" stroke="#fcc100" stroke-width="1.6"><path d="M3 12l9-9h8v8l-9 9z"/><path d="M9 12h6M9 15h4"/></svg></div>
  <div class="icon" style="left:956px;top:571px"><svg width="30" height="30" viewBox="0 0 24 24" fill="none" stroke="#fcc100" stroke-width="1.6"><circle cx="12" cy="10" r="6"/><path d="M8.5 15l-2 7 5.5-3 5.5 3-2-7"/></svg></div>

  <div class="feat" style="left:348px;top:266px"><h4>Licensed Experts</h4><p>Sed ut perspiciatis unde omnis iste natus error sit voluptatem accusantium doloremque laudantium, totam rem</p></div>
  <div class="feat right" style="left:613px;top:263px"><h4>24/7 Service Available</h4><p style="text-align:center">Sed ut perspiciatis unde omnis iste natus error sit voluptatem accusantium doloremque laudantium, totam rem aperiam,</p></div>
  <div class="feat" style="left:277px;top:416px"><h4>Labour Guaranteed</h4><p>Sed ut perspiciatis unde omnis iste natus error sit voluptatem accusantium doloremque laudantium, totam rem</p></div>
  <div class="feat right" style="left:687px;top:416px"><h4>Special Offers</h4><p>Sed ut perspiciatis unde omnis iste natus error sit voluptatem accusantium audantium, totam rem aperiam, eaque</p></div>
  <div class="feat" style="left:269px;top:568px"><h4>Fixed Fee Pricing</h4><p>Sed ut perspiciatis unde omnis iste natus error sit voluptatem accusantium doloremque laudantium, totam rem</p></div>
  <div class="feat right" style="left:699px;top:568px"><h4>100% Satisfatio Guaranteed</h4><p>Sed ut perspiciatis unde omnis iste natus error sit voluptatem accusantium doloremque laudantium, totam rem aperiam,</p></div>
</section>

<!-- Testimonials -->
<section class="testi">
  <div class="photo" role="img" aria-label="Faint signal strength decoration" style="left:0;top:105px;width:200px;height:330px;background:linear-gradient(90deg,rgba(130,110,40,.35),rgba(80,80,80,.18))"></div>
  <div class="label" style="top:76px">Our Client Testimonials</div>
  <h2 class="heading" style="top:92px">Eiusmod Tempor Incididunt Ut Labore Et Dolore</h2>
  <svg class="rule" style="top:128px" viewBox="0 0 48 12"><path d="M4 10h40M14 4h20" stroke="#fcc100" stroke-width="2"/></svg>
  <div class="review" style="left:205px">
    <div class="avatar" role="img" aria-label="Client portrait" style="background:linear-gradient(160deg,#c9b39a,#6e5f52)"></div>
    <div class="name">John Deo</div>
    <div class="role">Lorem Ipsum set <span class="stars">★★★★★</span></div>
    <p>Nemo enim ipsam voluptatem quia voluptas sit aspernatur aut odit aut fugit, sed quia consequuntur magni dolores eos qui ratione voluptatem seqnesciuntodit aut fugit, sed quia consequuntur magni.</p>
    <span class="quote">“</span>
    <span class="corner"></span>
  </div>
  <div class="review" style="left:617px">
    <div class="avatar" role="img" aria-label="Client portrait" style="background:linear-gradient(160deg,#b8c1c9,#56636e)"></div>
    <div class="name">John Deo</div>
    <div class="role">Lorem Ipsum set <span class="stars">★★★★★</span></div>
    <p>Nemo enim ipsam voluptatem quia voluptas sit aspernatur aut odit aut fugit, sed quia consequuntur magni dolores eos qui ratione voluptatem seqnesciuntodit aut fugit, sed quia consequuntur magni.</p>
    <span class="quote">“</span>
    <span class="corner"></span>
  </div>
  <div class="btn" style="left:531px;top:434px;width:138px;height:37px">View All</div>
</section>

<!-- Case studies -->
<section class="cases">
  <div class="label" style="top:72px">Our Case Studies</div>
  <h2 class="heading" style="top:88px">Eiusmod Tempor Incididunt Ut Labore Et Dolore</h2>
  <svg class="rule" style="top:124px" viewBox="0 0 48 12"><path d="M4 10h40M14 4h20" stroke="#fcc100" stroke-width="2"/></svg>

  <div class="case" style="left:208px;top:169px;width:251px;height:163px">
    <div class="date">JAN 14 2023</div>
    <h5>Lorem ipsum dolor sit amet, consectetur.</h5>
    <p>Lorem ipsum dolor sit amet, consectetur adipiscing elit sed do eiusmod.</p>
    <div class="more">LEARN MORE</div>
  </div>
  <div class="photo" role="img" aria-label="Hands holding a smartphone with floating app icons" style="left:476px;top:169px;width:250px;height:167px;background:linear-gradient(135deg,#2a6f9a,#a8d6ea 55%,#e7f2f7)"></div>
  <div class="case" style="left:740px;top:169px;width:250px;height:163px">
    <div class="date">JAN 14 2023</div>
    <h5>Lorem ipsum dolor sit amet, consectetur.</h5>
    <p>Lorem ipsum dolor sit amet, consectetur adipiscing elit sed do eiusmod.</p>
    <div class="more">LEARN MORE</div>
  </div>

  <div class="photo" role="img" aria-label="Hand holding a phone surrounded by blue network icons" style="left:208px;top:332px;width:251px;height:168px;background:linear-gradient(135deg,#0c2c5a,#3f86c7 55%,#b9d9f2)"></div>
  <div class="case" style="left:476px;top:336px;width:250px;height:164px">
    <div class="date">JAN 14 2023</div>
    <h5>Lorem ipsum dolor sit amet, consectetur.</h5>
    <p>Lorem ipsum dolor sit amet, consectetur adipiscing elit sed do eiusmod.</p>
    <div class="more">LEARN MORE</div>
  </div>
  <div class="photo" role="img" aria-label="Person using a smartphone on a busy city street" style="left:740px;top:332px;width:250px;height:168px;background:linear-gradient(135deg,#d08a4a,#6f6a66 50%,#1d5f6a)"></div>
</section>

<!-- Contact -->
<section class="contact">
  <div class="label" style="top:78px">Get in Touch</div>
  <h2 class="heading" style="top:94px">Eiusmod Tempor Incididunt Ut Labore Et Dolore</h2>
  <svg class="rule" style="top:130px" viewBox="0 0 48 12"><path d="M4 10h40M14 4h20" stroke="#fcc100" stroke-width="2"/></svg>
  <div class="photo" role="img" aria-label="Faint signal strength decoration" style="left:1010px;top:230px;width:190px;height:250px;background:linear-gradient(90deg,rgba(80,80,80,.2),rgba(130,110,40,.35))"></div>
  <div class="contact-box">
    <div class="input" style="left:49px;top:45px;width:309px;height:39px">First name</div>
    <div class="input" style="left:370px;top:45px;width:311px;height:39px">Last Name</div>
    <div class="input" style="left:49px;top:98px;width:309px;height:38px">Phone Numbers</div>
    <div class="input" style="left:370px;top:98px;width:311px;height:38px">Email address</div>
    <div class="input" style="left:49px;top:151px;width:632px;height:71px">Message</div>
    <div class="btn" style="left:296px;top:249px;width:138px;height:37px;background:#fff">Submit Now</div>
  </div>
</section>

<!-- Footer -->
<footer class="footer">
  <div class="abs" style="left:249px;top:78px;display:flex;flex-direction:column;align-items:flex-start">
    <div style="display:flex;align-items:center;gap:8px;font:500 24px var(--head);color:#fff"><span style="width:14px;height:14px;background:var(--yellow)"></span>Open Meadow</div>
    <div style="margin-top:4px;font:500 10px var(--body);color:var(--yellow)">MOBILE SIGNAL BOOSTER</div>
  </div>
  <div class="fcol abs" style="left:466px;top:14px">
    <h6>QUICK LINKS</h6>
    <ul><li>Home</li><li>Solutions</li><li>How it Works</li><li>Case Studies</li><li>Contact</li></ul>
  </div>
  <div class="fcol abs" style="left:647px;top:14px">
    <h6>LEGAL</h6>
    <ul><li>Terms of Use</li><li>Privacy Policy</li><li>Gallery</li><li>Contact Us</li></ul>
  </div>
  <div class="fcol plain abs" style="left:807px;top:14px;width:190px">
    <h6>CONTACT US</h6>
    <ul>
      <li style="display:flex;gap:8px;line-height:17px"><svg width="9" height="11" viewBox="0 0 8 10" style="flex:none;margin-top:2px"><path d="M4 0a4 4 0 0 1 4 4c0 3-4 6-4 6S0 7 0 4a4 4 0 0 1 4-4z" fill="#fff"/></svg>123 Lorem ipsum dolor sit amet, consectetur adipiscing eli.</li>
      <li style="display:flex;gap:8px"><svg width="10" height="10" viewBox="0 0 24 24" style="flex:none"><path d="M6.6 10.8a15 15 0 0 0 6.6 6.6l2.2-2.2a1 1 0 0 1 1-.25 11.4 11.4 0 0 0 3.6.57 1 1 0 0 1 1 1V20a1 1 0 0 1-1 1A17 17 0 0 1 3 4a1 1 0 0 1 1-1h3.5a1 1 0 0 1 1 1c0 1.25.2 2.45.57 3.57a1 1 0 0 1-.25 1z" fill="#fff"/></svg>+1 888 888 8888</li>
      <li style="display:flex;gap:8px;margin-top:16px"><svg width="11" height="9" viewBox="0 0 10 8" style="flex:none"><rect width="10" height="8" rx="1" fill="#fff"/><path d="M0 1l5 3.5L10 1" stroke="#0e0e0e" fill="none"/></svg>info@openmeadow.com</li>
    </ul>
  </div>
  <div class="abs" style="left:240px;top:163px;width:748px;height:1px;background:#444"></div>
  <div class="abs" style="left:0;top:182px;width:1200px;text-align:center;font:400 9.5px var(--body);color:#ddd">© copyrights 2023 | <span style="color:var(--yellow)">Open Meadow</span> | &nbsp;&nbsp;&nbsp;&nbsp; All rights reserved.</div>
</footer>

</div>
</body>
</html>
```